Lena Harcourt Tennis Academy - New Website

Our business is built around classes for all ages, competitions, and court hire.

There are a few gym style Wordpress templates that I think will have most of the functionality we need, but we don't like the style. We are looking for someone to make us a design that can be implemented as a child theme to one of these gym based Wordpress themes.

We have looked at:

http://plinthmarket.example/item/active-studio-responsive-wordpress-theme/full_screen_preview/7318264?ref=BrixoPages
http://www.vardel-skins.example/item/gym-fitness/demo/?r=brixopages
http://www.drumo.example/redirect/?theme=movewell

For style we are looking for something fresh, clean, and vibrant. Our logo is teal and gold with some red, orange, green and yellow.

https://huewheel.example/Citrus-Dawn-color-theme-738415/
https://huewheel.example/Mint-Frost-color-theme-604927/
https://huewheel.example/Solvane-color-theme-83051/

These are the colour schemes we are leaning towards.

Our current website can be seen here www.lhta-courts.example
Updates

The new logo design will be uploaded shortly. We don't need any more work done on that.

A rough logo file has been added for you to work with.

Could I please get some submissions that include what the other pages on the website will look like (instead of just the home page).

I think it's really important that we get the look of the product page. See the design pdf for our ideas on the layout of those pages.

***Edit*** Single product pages, I mean. I think the "Classes" page itself will be based a lot on the theme used so I'm less concerned about that. I just want to see what a page will look like that is only for.... Twilight Rally (for example)

Target Market(s)

We teach a lot of kids but also many comp players. Everything needs to be very clear and easy to navigate.

Industry/Entity Type

Court

Requirements
Must have
• Custom content types to easily post new things (eg, new programs, new coaches)
Timetable page that is dynamic based on the programs custom type.
Programs page that is dynamic based on the programs custom type.
Coaches page that is dynamic based on the coaches/trainers content type.

Page templates for programs, competitions and a few other things as per pdf.

```html
<!DOCTYPE html>
<html lang="en">
<head>
<meta charset="utf-8">
<title>Lena Harcourt Tennis Academy</title>
<link href="https://fonts.googleapis.com/css2?family=Roboto:wght@300;400;500&family=Maven+Pro:wght@600&display=swap" rel="stylesheet">
<style>
:root{
  --page:#f1f1f1;
  --teal:#2f7f95;
  --teal-dark:#1f5a6b;
  --gold:#e3b400;
  --gold-dark:#8a6d00;
  --green:#8cc100;
  --green-dark:#4f7000;
  --orange:#ff9500;
  --panel:#6c9fb8;
  --panel-light:#8db6c9;
  --ink:#333;
  --white:#fff;
}
*{margin:0;padding:0;box-sizing:border-box}
html,body{width:1043px;height:1200px;overflow:hidden;background:var(--page);font-family:'Roboto',sans-serif;color:var(--ink)}
.canvas{position:relative;width:1043px;height:1200px}
.abs{position:absolute}

.social{top:10px;width:28px;height:28px;border-radius:50%;background:var(--teal)}
.search{left:730px;top:11px;width:169px;height:25px;background:var(--white);border:1px solid #e2e2e2;font-size:8px;color:#aaa;padding:8px 8px 0}
.search-btn{left:905px;top:11px;width:34px;height:25px;background:var(--gold)}
.search-btn svg{display:block;margin:6px auto}

.logo{left:103px;top:38px}
.logo-name{font-family:'Maven Pro',sans-serif;font-weight:600;font-size:25px;line-height:28px;color:var(--teal);letter-spacing:1px;text-transform:uppercase}
.logo-tag{font-size:9px;color:#777;margin-top:2px;padding-left:80px}
.racket-art{left:853px;top:48px;width:86px;height:60px;border-radius:6px;background:linear-gradient(135deg,#2d84c4,#7fc0e6 60%,#f0a020)}

.nav{left:104px;top:112px;width:835px;height:52px;font-size:11.3px;color:var(--white);white-space:nowrap}
.nav a,.nav span{position:absolute;top:19px;color:inherit;text-decoration:none;white-space:nowrap}
.nav-bg{position:absolute;top:0;height:52px}
.nav-bg.programs{left:0;width:64px;background:var(--teal);border-bottom:6px solid var(--teal-dark)}
.nav-bg.main{left:64px;width:695px;background:var(--gold);border-bottom:6px solid var(--gold-dark)}
.nav-bg.enroll{left:759px;width:76px;background:var(--green);border-bottom:6px solid var(--green-dark)}
.nav .enroll-link{font-weight:500;font-size:11px}

.hero{left:0;top:178px;width:1043px;height:371px;background:radial-gradient(ellipse at 45% 55%,#6a7a2a 0,#4a4a40 18%,#5c4f58 40%,#b07a3e 75%,#d99a50 100%)}
.hero-title{left:582px;top:354px;font-size:52px;font-weight:300;color:var(--white);line-height:1;white-space:nowrap}
.dot{top:486px;width:16px;height:16px;border-radius:50%;background:radial-gradient(circle at 35% 35%,#fff,#aaa)}
.dot.active{background:radial-gradient(circle at 35% 35%,#ff5a5a,#c00000)}

.cta-text{left:263px;top:572px;font-size:31px;font-weight:300;color:#444;white-space:nowrap}
.cta-btn{left:569px;top:567px;width:209px;height:52px;background:linear-gradient(#ffa010,#ff8a00);color:var(--white);font-size:21px;font-weight:500;text-align:center;line-height:52px;box-shadow:0 2px 3px rgba(0,0,0,.2)}

.card{top:633px;width:262px;height:158px;box-shadow:0 8px 8px -6px rgba(0,0,0,.25)}
.card-photo{height:114px}
.card-label{height:44px;padding:14px 0 0 14px;font-size:15px;font-weight:500;color:#3a3a00;text-transform:uppercase}
.card-cardio .card-photo{background:linear-gradient(#3e6a3a,#8aa07a)}
.card-cardio .card-label{background:linear-gradient(#ffd070,#ff8a00)}
.card-court .card-photo{background:linear-gradient(#d8dde0,#3ea8c0 70%,#2b8aa6)}
.card-court .card-label{background:linear-gradient(#d9ec70,#82bb00)}
.card-rally .card-photo{background:linear-gradient(#4f7a3a,#9ab88a 60%,#d8d0c8)}
.card-rally .card-label{background:linear-gradient(#ffe870,#f5b800)}
.slide-arrow{top:700px}

.panel{top:832px;width:262px;height:263px;background:linear-gradient(135deg,var(--panel) 55%,var(--panel-light) 56%,var(--panel) 100%);color:var(--white)}
.panel-title{left:15px;top:24px;font-size:16px;font-weight:400;white-space:nowrap}
.pom-photo{left:17px;top:55px;width:228px;height:114px;background:linear-gradient(#d9b39a,#b84e3a 60%,#2d4a8a)}
.pom-name{left:10px;top:184px;font-size:12.5px}
.pom-quote{left:10px;top:203px;font-size:10.5px;white-space:nowrap}
.btn-small{left:9px;top:228px;width:79px;height:26px;background:var(--orange);font-size:12px;text-align:center;line-height:26px}
.post{left:14px;font-size:12px;line-height:13px;white-space:nowrap}
.post i{display:inline-block;width:11px;height:11px;border-radius:50%;background:radial-gradient(circle at 35% 35%,#e8ff80,#8cbf00);margin-right:11px;vertical-align:-1px}
.post small{display:block;font-size:9.5px;font-weight:300;color:#e4eef3;padding-left:22px}
.event{left:17px;width:240px}
.date{position:absolute;left:0;top:0;width:36px;height:34px;background:var(--gold);text-align:center;font-size:16px;line-height:15px;padding-top:3px}
.date span{display:block;font-size:11px;line-height:10px}
.date-year{position:absolute;left:7px;top:36px;font-size:9.5px}
.event-title{position:absolute;left:48px;top:0;font-size:12px;white-space:nowrap}
.event-body{position:absolute;left:48px;top:27px;font-size:9.6px;font-weight:300;line-height:17px;color:#e4eef3;white-space:nowrap}
.event-body b{font-weight:400;color:var(--white);font-size:10.5px}

.footer-line{left:0;top:1117px;width:1043px;border-top:1px solid #e4e4e4}
.footer-nav{left:0;top:1119px;width:1043px;text-align:center;font-size:12px;color:#444;font-weight:300;white-space:nowrap}
.footer-nav span{margin:0 11px}
.copyright{left:0;top:1151px;width:1043px;text-align:center;font-size:11.5px;color:#444;font-weight:300}
</style>
</head>
<body>
<div class="canvas">

  <div class="abs social" style="left:626px"></div>
  <div class="abs social" style="left:660px"></div>
  <div class="abs social" style="left:693px"></div>
  <div class="abs search">Search</div>
  <div class="abs search-btn"><svg width="12" height="12" viewBox="0 0 12 12"><circle cx="4.5" cy="4.5" r="3" fill="none" stroke="#fff" stroke-width="1.6"/><line x1="6.8" y1="6.8" x2="11" y2="11" stroke="#fff" stroke-width="1.8"/></svg></div>

  <div class="abs logo">
    <div class="logo-name">Lena Harcourt<br>Tennis Academy</div>
    <div class="logo-tag">reach your potential</div>
  </div>
  <div class="abs racket-art" role="img" aria-label="Painted tennis racket illustration on a blue brush stroke"></div>

  <nav class="abs nav">
    <div class="nav-bg programs"></div>
    <div class="nav-bg main"></div>
    <div class="nav-bg enroll"></div>
    <a href="#" style="left:9px">Programs</a>
    <a href="#" style="left:76px">Competitions</a>
    <a href="#" style="left:160px">Court Hire</a>
    <a href="#" style="left:228px">Restrings</a>
    <a href="#" style="left:293px">Gallery</a>
    <a href="#" style="left:345px">Schedule</a>
    <a href="#" style="left:409px">Player of the Month</a>
    <a href="#" style="left:528px">Contact Us</a>
    <a href="#" style="left:598px">About</a>
    <a href="#" style="left:643px">Locations</a>
    <span style="left:722px">▼</span>
    <a class="enroll-link" href="#" style="left:762px">ENROLL NOW</a>
  </nav>

  <div class="abs hero" role="img" aria-label="Close-up photo of a tennis ball resting on a clay court at dusk"></div>
  <div class="abs hero-title">What we do ?</div>
  <div class="abs dot active" style="left:480px"></div>
  <div class="abs dot" style="left:502px"></div>
  <div class="abs dot" style="left:523px"></div>
  <div class="abs dot" style="left:545px"></div>

  <div class="abs cta-text">Did you know you can</div>
  <div class="abs cta-btn">ENROLL ONLINE</div>

  <svg class="abs slide-arrow" style="left:82px" width="16" height="24" viewBox="0 0 16 24"><polyline points="13,2 3,12 13,22" fill="none" stroke="#666" stroke-width="2.5"/></svg>
  <div class="abs card card-cardio" style="left:113px"><div class="card-photo" role="img" aria-label="Player hitting a forehand on an outdoor court"></div><div class="card-label">Cardio</div></div>
  <div class="abs card card-court" style="left:391px"><div class="card-photo" role="img" aria-label="Indoor hall with blue tennis courts"></div><div class="card-label">Hire a Court</div></div>
  <div class="abs card card-rally" style="left:668px"><div class="card-photo" role="img" aria-label="Group of players relaxing courtside among trees"></div><div class="card-label">Twilight Rally</div></div>
  <svg class="abs slide-arrow" style="left:943px" width="16" height="24" viewBox="0 0 16 24"><polyline points="3,2 13,12 3,22" fill="none" stroke="#666" stroke-width="2.5"/></svg>

  <section class="abs panel" style="left:113px">
    <h2 class="abs panel-title">Player Of The Month</h2>
    <div class="abs pom-photo" role="img" aria-label="Coach with two young players holding a trophy"></div>
    <div class="abs pom-name">Toby Marsh</div>
    <div class="abs pom-quote">Hard work and determination really do pay off!</div>
    <div class="abs btn-small">Read More</div>
  </section>

  <section class="abs panel" style="left:391px">
    <h2 class="abs panel-title" style="top:27px">Recent Post List</h2>
    <div class="abs post" style="top:60px"><i></i>Rain Make Ups Term 3-2013<small>Posted by milo - August 15, 2013</small></div>
    <div class="abs post" style="top:109px"><i></i>Holler for a Hoodie Winners<small>Posted by milo - August 15, 2013</small></div>
    <div class="abs post" style="top:158px"><i></i>Friday Ladies Comp<small>Posted by milo - August 15, 2013</small></div>
    <div class="abs post" style="top:213px"><i></i>Holler For A Hoodie<small>Posted by milo - August 15, 2013</small></div>
  </section>

  <section class="abs panel" style="left:668px">
    <h2 class="abs panel-title" style="left:19px">Upcoming Events</h2>
    <div class="abs event" style="top:50px">
      <div class="date">02<span>SEP</span></div><div class="date-year">2013</div>
      <div class="event-title">Player of the Month Nominations</div>
      <div class="event-body">Player of the month nominations can now<br>be made through the "Contact Us" page.<br>(Hover over "About" on the menu) Just<br>select &nbsp;&nbsp;&nbsp;&nbsp;... <b>Read More</b></div>
    </div>
    <div class="abs event" style="top:156px">
      <div class="date">02<span>SEP</span></div><div class="date-year">2013</div>
      <div class="event-title">New Feature: Social Media Login!</div>
      <div class="event-body">Player of the month nominations can ow<br>be made through the "Contact Us" page.<br>(Hover over "About" on the menu) Just<br>select &nbsp;&nbsp;&nbsp;&nbsp;... <b>Read More</b></div>
    </div>
  </section>

  <div class="abs footer-line"></div>
  <div class="abs footer-nav">Competitions<span>|</span>Court Hire<span>|</span>Restrings<span>|</span>Gallery<span>|</span>Schedule<span>|</span>Player of the Month<span>|</span>Contact Us</div>
  <div class="abs copyright">© Copyright 2013 .All rights Reserved</div>

</div>
</body>
</html>
```